Toy company needs a banner design

I need a banner design to go on my Facebook and website home page. I already have a logo, the banner needs to be in some kinds of relation to my logo, or just photos to match my products. We manufacture and wholesale stuffed animals, the customization is the key feature. Sewn at Quillbury is our company name and we are trying to give the message of our unique designed and high quality products, environmental friendly materials and customization on almost every piece.

Target Market(s)

Corporate gifts, individual gifts (birthday, anniversary, graduation, wedding)

Industry/Entity Type

Toy Store

Logo Text

Plush Harbor Pals

Number of Pages Required

5+ page

Logo styles of interest
Abstract Logo
Font styles to use
Decorative

Requirements
Nice to have
• toy pictures or drawings

```html
<!DOCTYPE html>
<html lang="en">
<head>
<meta charset="utf-8">
<title>Soft Lifestyle Banner</title>
<link rel="stylesheet" href="https://fonts.googleapis.com/css2?family=Jost:wght@300;400&display=swap">
<style>
  :root {
    --page-bg: #ececec;
    --banner-white: #ffffff;
    --banner-shade: #f3f3f3;
    --brand-red: #d8402a;
    --soft-red: #e98a80;
    --ink: #111111;
    --name-blue: #3ea8d4;
    --plush-tan: #c89a62;
    --plush-brown: #8a5a32;
  }
  html, body {
    margin: 0;
    width: 1200px;
    height: 1200px;
    overflow: hidden;
    background: var(--page-bg);
    font-family: "Jost", sans-serif;
  }
  .banner {
    position: absolute;
    left: 50px;
    top: 397px;
    width: 1100px;
    height: 407px;
    background: linear-gradient(180deg, var(--banner-white) 0%, var(--banner-white) 70%, var(--banner-shade) 100%);
    overflow: hidden;
  }
  .banner-art {
    position: absolute;
    inset: 0;
    width: 100%;
    height: 100%;
  }
  .brand-name {
    position: absolute;
    left: 30px;
    top: 40px;
    width: 130px;
    display: flex;
    align-items: flex-start;
    gap: 8px;
    color: var(--name-blue);
    font-weight: 400;
    font-size: 22px;
    line-height: 1.05;
  }
  .brand-dot {
    flex: none;
    width: 14px;
    height: 14px;
    margin-top: 4px;
    border-radius: 50%;
    background: var(--brand-red);
  }
  .headline {
    position: absolute;
    left: 474px;
    top: 18px;
    margin: 0;
    color: var(--ink);
    font-weight: 400;
    font-size: 104px;
    line-height: 1;
    letter-spacing: 1px;
  }
  .tagline {
    position: absolute;
    left: 480px;
    top: 128px;
    margin: 0;
    color: var(--brand-red);
    font-weight: 400;
    font-size: 29px;
    line-height: 1;
    letter-spacing: 0.3px;
  }
</style>
</head>
<body>
  <section class="banner">
    <svg class="banner-art" viewBox="0 0 945 350" preserveAspectRatio="none" xmlns="http://www.w3.org/2000/svg">
      <defs>
        <linearGradient id="plush-group" x1="0" y1="0" x2="1" y2="1">
          <stop offset="0" stop-color="#d7ad74"/>
          <stop offset="0.5" stop-color="#a9743f"/>
          <stop offset="1" stop-color="#e6c49a"/>
        </linearGradient>
        <radialGradient id="pony-fill"><stop offset="0" stop-color="#f4efe8"/><stop offset="1" stop-color="#b98a63"/></radialGradient>
        <radialGradient id="bear-fill"><stop offset="0" stop-color="#b4454a"/><stop offset="1" stop-color="#c79a6a"/></radialGradient>
        <radialGradient id="monkey-fill"><stop offset="0" stop-color="#6f6a66"/><stop offset="1" stop-color="#d8d4d0"/></radialGradient>
      </defs>

      <path class="sweep-soft" d="M128 -5 Q300 60 420 250" fill="none" stroke="var(--soft-red)" stroke-width="34"/>
      <path class="sweep-strong" d="M190 -5 Q340 60 440 215" fill="none" stroke="var(--brand-red)" stroke-width="20"/>
      <path class="link-line" d="M420 250 Q640 300 945 283" fill="none" stroke="var(--brand-red)" stroke-width="3"/>

      <rect class="plush-photo" role="img" aria-label="Photo of four plush toys: giraffe, tiger, monkey and lion" x="22" y="128" width="345" height="205" rx="30" fill="url(#plush-group)"/>

      <g class="product-ring">
        <circle cx="467" cy="238" r="76" fill="var(--banner-white)" stroke="var(--brand-red)" stroke-width="7"/>
        <circle role="img" aria-label="Photo of a plush pony" cx="467" cy="238" r="58" fill="url(#pony-fill)"/>
      </g>
      <g class="product-ring">
        <circle cx="654" cy="236" r="86" fill="var(--banner-white)" stroke="var(--brand-red)" stroke-width="7"/>
        <circle role="img" aria-label="Photo of a teddy bear holding a flag heart" cx="654" cy="236" r="66" fill="url(#bear-fill)"/>
      </g>
      <g class="product-ring">
        <circle cx="837" cy="238" r="76" fill="var(--banner-white)" stroke="var(--brand-red)" stroke-width="7"/>
        <circle role="img" aria-label="Photo of a sock monkey in a graduation cap" cx="837" cy="238" r="58" fill="url(#monkey-fill)"/>
      </g>

      <rect class="base-bar" x="0" y="342" width="945" height="8" fill="var(--brand-red)"/>
    </svg>

    <div class="brand-name"><span class="brand-dot"></span><span>Sewn at Quillbury</span></div>
    <h1 class="headline">Soft Lifestyle</h1>
    <p class="tagline">Eco friendly materials for happier earth</p>
  </section>
</body>
</html>
```